Modern Employee Handbook Cover Design Needed

I need help. I am designing a 50+ page Employee Handbook and want a great cover design. I'm looking for a great cover because our company has changed so much in the past years since the last handbook was published and I want to signify and celebrate all the positive things we have done. It may not seem like such a big deal but I'm trying to make a big impact.

I'm looking for something interesting. Employee Handbooks are the most boring things int he world but I don't ours to LOOK that way. I want creative, modern, slick, clean, whatever you want that would make someone want to look at (even if it is for a second). It does NOT need to even be called an Employee Handbook (I'm really open to ideas)

This will be a typical 8.5 x 11 book format. 70% of our employees are under the age of 40 and are in CA, MA, FL, and IN.

The final design should communicate that we are not the same company we were a few years ago but instead we are more modern and current.

Target Market(s)

Most of our employees are under 40 years old. They are well educated. We are a national company with employees in CA, MA, FL and IN

Industry/Entity Type

Education

Font styles to use
Serif
Sans Serif
Other font styles liked:
• I like the fonts used by tovrin but am open to ANY fonts.

Requirements
Must have
• Modern, up to date designs, unexpected, unique, cool, etc...
Should not have
• I don't like the typical teamwork images, world and globe things, or tree supporting branch type things that Human Resources and Employee Handbooks often is represented by in print. They are so boring to me. https://www.quelvor.com/find?q=human+resources+handbook&src=lnms&mode=img&sa=X&ref=0bhVKFxkm2pQYIu83SBjRMrd9KLwQ_BVJDDhC&vw=1920&vh=950
• No stick figures standing in a row or shaking hands. Stuff like that is so old.
• Our clients are young adults with Autism but I don't want puzzle pieces which is a universal symbol of Autism.

```html
<!DOCTYPE html>
<html lang="en">
<head>
<meta charset="utf-8">
<title>ORV Employee Handbook Cover</title>
<link rel="stylesheet" href="https://fonts.googleapis.com/css2?family=Archivo+Black&family=Source+Sans+3:wght@400;700&display=swap">
<style>
  :root {
    --bg-tint: #d3efec;
    --bg-white: #ffffff;
    --brand-blue: #1b3fc4;
    --tagline-blue: #2b9ae0;
    --accent-red: #e3262a;
    --ghost-blue: rgba(120, 170, 220, 0.10);
    --art-magenta: #e0249a;
    --art-orange: #ff6a1a;
    --art-yellow: #ffd21c;
    --art-green: #9be03a;
    --art-cyan: #4fd0ec;
  }
  html, body {
    margin: 0;
    padding: 0;
    overflow: hidden;
  }
  body {
    width: 924px;
    height: 1200px;
  }
  .cover {
    position: relative;
    width: 924px;
    height: 1200px;
    overflow: hidden;
    background: radial-gradient(ellipse at 20% 30%, var(--bg-tint) 0%, #e9f7f5 45%, var(--bg-white) 85%);
    font-family: "Source Sans 3", sans-serif;
  }
  .ghost-name {
    position: absolute;
    left: 175px;
    top: 840px;
    margin: 0;
    font-family: "Archivo Black", sans-serif;
    font-size: 420px;
    line-height: 1;
    letter-spacing: -6px;
    color: var(--ghost-blue);
  }
  .artwork {
    position: absolute;
    left: 0;
    top: 0;
    width: 924px;
    height: 1200px;
  }
  .title-block {
    position: absolute;
    left: 474px;
    top: 718px;
  }
  .brand-name {
    margin: 0;
    font-family: "Archivo Black", sans-serif;
    font-weight: 400;
    font-size: 150px;
    line-height: 140px;
    letter-spacing: -2px;
    color: var(--brand-blue);
  }
  .tagline {
    margin: 40px 0 0;
    font-weight: 700;
    font-size: 30px;
    line-height: 42px;
    color: var(--tagline-blue);
  }
  .doc-title {
    margin: 22px 0 0;
    font-weight: 400;
    font-size: 40px;
    line-height: 1;
    color: var(--accent-red);
  }
</style>
</head>
<body>
  <main class="cover">
    <p class="ghost-name" aria-hidden="true">ORV</p>

    <svg class="artwork" viewBox="0 0 924 1200" role="img" aria-label="Cascade of overlapping translucent diamonds in magenta, orange, yellow, green and cyan falling down the left side">
      <defs>
        <linearGradient id="cascade-fill" x1="0" y1="0" x2="0.3" y2="1">
          <stop offset="0" stop-color="var(--art-magenta)"/>
          <stop offset="0.25" stop-color="var(--art-orange)"/>
          <stop offset="0.5" stop-color="var(--art-yellow)"/>
          <stop offset="0.75" stop-color="var(--art-green)"/>
          <stop offset="1" stop-color="var(--art-cyan)"/>
        </linearGradient>
      </defs>
      <polygon points="110,0 610,0 560,250 420,520 360,760 330,960 300,1200 240,1200 150,960 120,700 110,420 100,200" fill="url(#cascade-fill)" opacity="0.85"/>
    </svg>

    <header class="title-block">
      <h1 class="brand-name">ORV</h1>
      <p class="tagline">Guiding Young Adults<br>Toward Independent Lives<br>and Careers Since 1991</p>
      <p class="doc-title">Employee Handbook</p>
    </header>
  </main>
</body>
</html>
```